Wind turbine blade repair business need short brochure design

We are Kestrel Height Services Ltd. Please see our website www.kestrelheightservices.co.uk. We need a brochure that describes the business services we offer. It needs to look sharp and professional. We are a rope access service provider who offer wind turbine rotor blade repair and inspection services. We are based and operate in Northern Ireland and the Republic of Ireland. Health and Safety is paramount in our industry and this should be emphasised.

```html
<!DOCTYPE html>
<html lang="en">
<head>
<meta charset="utf-8">
<title>Kestrel Height Services – Brochure</title>
<link href="https://fonts.googleapis.com/css2?family=Poppins:wght@400;500;600;700&display=swap" rel="stylesheet">
<style>
:root{
  --orange:#e0542b;
  --orange-deep:#c9461f;
  --black:#1b1b1c;
  --ink:#2a2a2a;
  --paper:#eeeeef;
  --bg:#e4e4e6;
  --white:#ffffff;
  --muted:#bdbdbd;
}
*{margin:0;padding:0;box-sizing:border-box}
html,body{width:1200px;height:3085px;overflow:hidden}
body{background:var(--bg);font-family:"Poppins",sans-serif;position:relative}
.spread{position:absolute;left:50px;width:1100px;height:715px;display:flex;box-shadow:0 12px 40px rgba(0,0,0,.18)}
.spread--outer{top:560px}
.spread--inner{top:1760px}
.page{position:relative;width:550px;height:715px;overflow:hidden}

/* brand stand-in */
.brand{display:flex;flex-direction:column;align-items:center;justify-content:center;gap:6px;background:var(--black);border:2px solid var(--white);color:var(--white);font-weight:600;font-size:10px;line-height:1.2;text-align:center;text-transform:uppercase}
.brand__dot{width:14px;height:14px;background:var(--orange)}

/* back cover */
.back{background:var(--orange)}
.back__content{position:absolute;left:0;right:0;top:250px;display:flex;flex-direction:column;align-items:center;color:var(--white);text-align:center}
.back .brand{width:92px;height:92px;margin-bottom:42px}
.back__title{font-size:21px;font-weight:700;letter-spacing:.5px;margin-bottom:18px}
.contact-item{display:flex;flex-direction:column;align-items:center;gap:6px;font-size:8.5px;margin-bottom:16px;line-height:1.35}
.contact-item svg{width:12px;height:12px;fill:var(--white)}

/* front cover */
.front{background:var(--black)}
.front .brand{position:absolute;left:42px;top:42px;width:86px;height:86px}
.front__title{position:absolute;left:152px;top:38px;color:var(--white);font-size:37px;font-weight:700;line-height:1.2;letter-spacing:.5px}
.front__photo{position:absolute;left:0;right:0;top:210px;bottom:0;background:linear-gradient(180deg,#2f5f9b 0%,#5a7fa8 40%,#7b6a55 75%,#3f3a35 100%)}
.front__tag{position:absolute;left:26px;bottom:72px;width:290px;color:var(--white);font-size:10.5px;font-weight:500;line-height:1.3;text-transform:uppercase}

/* inner left */
.services-page{background:linear-gradient(180deg,#f2f2f3,#e7e7e8)}
.services-page__photo{position:absolute;left:20px;top:0;width:510px;height:192px;border-radius:0 0 12px 12px;background:linear-gradient(135deg,#5d6c7d 0%,#8a8f8f 45%,#d66a2c 70%,#3a3d42 100%)}
.kicker{display:flex;align-items:flex-start;gap:8px;color:var(--orange);font-size:11px;font-weight:600;text-transform:uppercase;line-height:1.25}
.kicker svg{flex:none;width:15px;height:15px;margin-top:-1px}
.services-page .kicker{position:absolute;left:30px;top:222px;width:420px}
.services-page .kicker svg{stroke:var(--ink)}
.lead{font-size:7.5px;line-height:1.45}
.services-page .lead{position:absolute;left:32px;top:268px;width:470px;color:var(--ink)}
.pill{display:inline-block;padding:3px 10px;border-radius:6px;font-size:14.5px;font-weight:500;text-transform:uppercase;color:var(--white)}
.services-page .pill{position:absolute;left:32px;top:300px;background:var(--black);color:var(--orange)}
.services-grid{position:absolute;left:32px;top:350px;width:490px;display:grid;grid-template-columns:repeat(3,1fr);row-gap:22px}
.service{display:flex;align-items:center;gap:12px;font-size:7.5px;line-height:1.3;color:var(--ink);height:32px}
.service__icon{flex:none;width:30px;height:30px;border:2px solid var(--orange);border-radius:50%;position:relative}
.service__icon::after{content:"";position:absolute;inset:8px;border:2px solid var(--orange);border-radius:3px}

/* inner right */
.info-page{background:var(--black);color:var(--white);padding:36px 34px 0 34px}
.info-page .kicker svg{stroke:var(--white)}
.info-page .lead{color:#d8d8d8;margin-top:10px}
.info-page .pill{background:var(--orange);margin:22px 0 14px}
.info-page .lead + .lead{margin-top:8px}
.gallery{display:flex;gap:22px;margin:26px 0 22px}
.gallery__item{width:124px;height:98px;border-radius:6px}
.gallery__item--sky{background:linear-gradient(180deg,#9fb4c8,#4c5a68)}
.gallery__item--tower{background:linear-gradient(160deg,#c9c3b6,#6a8a56 60%,#d8642c)}
.gallery__item--night{background:linear-gradient(180deg,#2b3138,#dfe3e6)}
.about{width:300px}
.gear{position:absolute;right:0;bottom:40px;width:170px;height:120px;border-radius:50%;background:radial-gradient(circle at 35% 55%,#f07a2a 0%,#e0542b 30%,#c8b03a 60%,rgba(27,27,28,0) 72%)}
</style>
</head>
<body>

<section class="spread spread--outer">
  <div class="page back">
    <div class="back__content">
      <div class="brand"><span class="brand__dot"></span><span>Kestrel Height<br>Services</span></div>
      <h2 class="back__title">CONTACT US</h2>
      <div class="contact-item"><svg viewBox="0 0 24 24"><path d="M6.6 10.8a15 15 0 0 0 6.6 6.6l2.2-2.2c.3-.3.7-.4 1-.2 1.1.4 2.3.6 3.6.6.6 0 1 .4 1 1V20c0 .6-.4 1-1 1A17 17 0 0 1 3 4c0-.6.4-1 1-1h3.5c.6 0 1 .4 1 1 0 1.3.2 2.5.6 3.6.1.3 0 .7-.2 1z"/></svg><span>+44 (0)28 9000 0123</span></div>
      <div class="contact-item"><svg viewBox="0 0 24 24"><path d="M2 5h20v14H2zM3 6l9 7 9-7"/></svg><span>info@kestrelheightservices.co.uk</span></div>
      <div class="contact-item"><svg viewBox="0 0 24 24"><path d="M12 2a7 7 0 0 0-7 7c0 5 7 13 7 13s7-8 7-13a7 7 0 0 0-7-7zm0 9.5A2.5 2.5 0 1 1 12 6.5a2.5 2.5 0 0 1 0 5z"/></svg><span>12 Harbour Lane, Ballyholme,<br>County Down, Northern Ireland,<br>BT20 5QQ.</span></div>
      <div class="contact-item"><svg viewBox="0 0 24 24"><circle cx="12" cy="12" r="10"/></svg><span>www.kestrelheightservices.co.uk</span></div>
    </div>
  </div>
  <div class="page front">
    <div class="brand"><span class="brand__dot"></span><span>Kestrel Height<br>Services</span></div>
    <h1 class="front__title">QUALITY,SAFETY,<br>RESULTS</h1>
    <div class="front__photo" role="img" aria-label="Rope access technician in orange hi-vis and helmet working on ropes high above a town"></div>
    <p class="front__tag">Kestrel Height Services provides specialist rope access and work at height services to the construction, maintenance and renewable sectors.</p>
  </div>
</section>

<section class="spread spread--inner">
  <div class="page services-page">
    <div class="services-page__photo" role="img" aria-label="Close-up of a technician in orange hi-vis checking harness gear at height"></div>
    <div class="kicker"><svg viewBox="0 0 16 16" fill="none" stroke-width="1.4"><circle cx="8" cy="8" r="6.5"/><path d="M7 5l3 3-3 3"/></svg><span>Rope access, work at height, wind turbine services, geo-technical</span></div>
    <p class="lead">Kestrel Height Services believes in keeping your project as simple and straightforward as possible regardless of how complex the task may seem.</p>
    <span class="pill">Services we offer</span>
    <div class="services-grid">
      <div class="service"><span class="service__icon"></span>Access<br>solutions</div>
      <div class="service"><span class="service__icon"></span>Concrete rendering<br>and repair</div>
      <div class="service"><span class="service__icon"></span>Consultancy</div>
      <div class="service"><span class="service__icon"></span>Cladding<br>and glazing</div>
      <div class="service"><span class="service__icon"></span>Confined Space<br>Entry</div>
      <div class="service"><span class="service__icon"></span>Geotechnical<br>services</div>
      <div class="service"><span class="service__icon"></span>Inspection<br>and testing</div>
      <div class="service"><span class="service__icon"></span>Load testing</div>
      <div class="service"><span class="service__icon"></span>Rigging</div>
      <div class="service"><span class="service__icon"></span>IRATA L3<br>supervision</div>
      <div class="service"><span class="service__icon"></span>Painting and<br>coating</div>
      <div class="service"><span class="service__icon"></span>Safety netting</div>
      <div class="service"><span class="service__icon"></span>Shutdown<br>services</div>
      <div class="service"><span class="service__icon"></span>Stand-by<br>rescue</div>
      <div class="service"><span class="service__icon"></span>Telecommunications</div>
      <div class="service"><span class="service__icon"></span>Sign installation</div>
      <div class="service"><span class="service__icon"></span>Surveys and<br>inspection</div>
      <div class="service"><span class="service__icon"></span>Wind turbine<br>maintenance</div>
    </div>
  </div>
  <div class="page info-page">
    <div class="kicker"><svg viewBox="0 0 16 16" fill="none" stroke-width="1.4"><circle cx="8" cy="8" r="6.5"/><path d="M7 5l3 3-3 3"/></svg><span>Fast, safe and efficient</span></div>
    <p class="lead">Industrial rope access is a safe method of working at height where ropes and associated equipment are used to gain access to and from the work position.</p>
    <span class="pill">Rope access solutions</span>
    <p class="lead">The advantage of using rope access methods mainly lies in the safety and speed with which workers can get to or from difficult locations in order to carry out their work, often with minimal impact on other operations, surrounding areas and the environment.</p>
    <p class="lead">Another major benefit is the reduction of the combination of the total man-hours and perceived level of risk for a particular task (man-at-risk hours) when compared with other means of access and their associated risks and costs.</p>
    <div class="gallery">
      <div class="gallery__item gallery__item--sky" role="img" aria-label="Wind turbines on the horizon under a cloudy sky"></div>
      <div class="gallery__item gallery__item--tower" role="img" aria-label="Technician descending a tower on ropes"></div>
      <div class="gallery__item gallery__item--night" role="img" aria-label="Technician working beneath a large structure"></div>
    </div>
    <div class="kicker"><svg viewBox="0 0 16 16" fill="none" stroke-width="1.4"><circle cx="8" cy="8" r="6.5"/><path d="M7 5l3 3-3 3"/></svg><span>Professional, dependable, innovative</span></div>
    <p class="lead">Kestrel Height Services is a Northern Irish based company providing specialist access, work at height, and service solutions throughout Ireland and the UK.</p>
    <span class="pill">About Kestrel Height Services</span>
    <div class="about">
      <p class="lead">With a combined experience of 30 years within rope access, we have knowledge, skills and experience in a wide range of industry sectors.</p>
      <p class="lead">We are committed to providing a safe, consistent and professional service. We are passionate about finding the most effective solution to our clients' access problems and delivering the results on time and within budget.</p>
      <p class="lead">Our ambition is to be the rope access company of choice throughout Ireland and the United Kingdom. Through our commitment to health and safety, the care of the environment, and our aim to deliver beyond expectations, we believe we can fulfil our ambition.</p>
    </div>
    <div class="gear" role="img" aria-label="Orange safety helmet with coiled climbing rope"></div>
  </div>
</section>

</body>
</html>
```